Accommodation business card design

We need a business card designed for our long-term accommodation business based in Australia. The business card must match the style of the attached letterhead and logo. The same contact details that are on the letterhead will also go on the card except that the card must list the contact details in the following order:phone, email, home address, ABN.

The card will be printed on .76mm white pvc plastic (same as credit cards), printed both sides and will be silver foil stamped on at least one side (preferably 2 sides) The design template is attached, but please go to www.zt.com.au for more specs.

The only other addition the card will be my name: Malcolm Darby

```html
<!DOCTYPE html>
<html lang="en">
<head>
<meta charset="utf-8">
<title>Ridgeway Accommodation – Business Card</title>
<link rel="stylesheet" href="https://fonts.googleapis.com/css2?family=Mulish:wght@400;600;900&display=swap">
<style>
  :root {
    --page-bg: #ece8e4;
    --gold-light: #d9bd7e;
    --gold: #c4a260;
    --gold-dark: #a9864a;
    --purple-deep: #6e1463;
    --purple: #8c1a7c;
    --magenta: #c21f8e;
    --maroon: #6b1a3c;
    --white: #ffffff;
  }
  * { box-sizing: border-box; margin: 0; padding: 0; }
  html, body {
    width: 1200px; height: 754px; overflow: hidden;
    background: var(--page-bg);
    font-family: "Mulish", sans-serif;
  }
  .sheet {
    position: relative; width: 1200px; height: 754px;
    display: flex; justify-content: center; align-items: center; gap: 60px;
  }
  .card {
    position: relative; width: 540px; height: 340px;
    border-radius: 18px; overflow: hidden;
    box-shadow: 0 10px 28px rgba(60, 30, 40, 0.28);
  }
  .card-bg { position: absolute; inset: 0; width: 100%; height: 100%; }

  .brand { position: absolute; display: flex; align-items: center; gap: 14px; }
  .brand-square {
    width: 68px; height: 68px; border-radius: 10px; background: var(--maroon);
  }
  .brand-name {
    color: var(--maroon); font-weight: 900; line-height: 1;
    text-transform: uppercase;
  }
  .brand-name .line-main { display: block; font-size: 40px; letter-spacing: 1px; }
  .brand-name .line-sub { display: block; font-size: 19px; letter-spacing: 0.5px; margin-top: 2px; }

  .card-front .brand { left: 40px; top: 34px; }
  .card-back .brand { left: 46px; top: 126px; }

  .holder-name {
    position: absolute; left: 232px; top: 158px;
    color: var(--white); font-size: 15px; font-weight: 600;
  }
  .postal {
    position: absolute; right: 22px; top: 172px; text-align: right;
    color: var(--white); font-size: 14px; line-height: 1.4;
  }
  .postal-icon { display: block; margin: 0 0 6px auto; width: 14px; height: 16px; }
  .contacts {
    position: absolute; left: 30px; top: 240px;
    list-style: none; color: var(--white); font-size: 14px;
  }
  .contacts li { display: flex; align-items: center; gap: 8px; height: 22px; }
  .contacts svg { width: 16px; height: 16px; flex: none; }
  .contacts .abn { padding-left: 24px; }
  .abn-label { color: var(--gold-light); margin-right: 4px; }
</style>
</head>
<body>
<main class="sheet">

  <article class="card card-front" aria-label="Business card front">
    <svg class="card-bg" viewBox="0 0 540 340" preserveAspectRatio="none" aria-hidden="true">
      <defs>
        <linearGradient id="goldFront" x1="0" y1="0" x2="1" y2="1">
          <stop offset="0" stop-color="var(--gold-dark)"/>
          <stop offset="0.5" stop-color="var(--gold-light)"/>
          <stop offset="1" stop-color="var(--gold)"/>
        </linearGradient>
        <radialGradient id="purpleFront" cx="0.5" cy="0.55" r="0.7">
          <stop offset="0" stop-color="var(--magenta)"/>
          <stop offset="1" stop-color="var(--purple-deep)"/>
        </radialGradient>
      </defs>
      <rect width="540" height="340" fill="url(#goldFront)"/>
      <path d="M0 150 C120 150 330 140 430 100 C390 135 300 158 260 160 L540 160 L540 340 L0 340 Z" fill="url(#purpleFront)"/>
      <path d="M0 140 C140 142 320 130 440 88 C400 118 310 142 200 150 L0 152 Z" fill="var(--purple)"/>
      <rect y="302" width="540" height="5" fill="var(--gold)"/>
      <rect y="318" width="540" height="12" fill="var(--gold)"/>
    </svg>

    <div class="brand">
      <span class="brand-square" aria-hidden="true"></span>
      <p class="brand-name"><span class="line-main">Ridgeway</span><span class="line-sub">Accommodation</span></p>
    </div>

    <p class="holder-name">Malcolm Darby</p>

    <address class="postal" style="font-style:normal">
      <svg class="postal-icon" viewBox="0 0 14 16" aria-hidden="true">
        <path d="M7 0a5 5 0 0 0-5 5c0 4 5 11 5 11s5-7 5-11a5 5 0 0 0-5-5z" fill="var(--white)"/>
        <circle cx="7" cy="5" r="2" fill="var(--purple)"/>
      </svg>
      PO Box 1180<br>Harbour Mail Centre<br>QLD 4700
    </address>

    <ul class="contacts">
      <li>
        <svg viewBox="0 0 16 16" aria-hidden="true">
          <circle cx="8" cy="8" r="8" fill="var(--white)"/>
          <path d="M5 4l2 2-1 1c.5 1.2 1.6 2.3 2.8 2.8l1-1 2 2-1.2 1.2C7.5 11.5 4.5 8.5 3.8 5.2z" fill="var(--purple)"/>
        </svg>
        0412 555 308
      </li>
      <li>
        <svg viewBox="0 0 16 16" aria-hidden="true">
          <circle cx="8" cy="8" r="8" fill="var(--white)"/>
          <rect x="4" y="5" width="8" height="6" fill="var(--purple)"/>
          <path d="M4 5l4 3.5L12 5" stroke="var(--white)" stroke-width="1" fill="none"/>
        </svg>
        malcolm.darby@mailbox.com.au
      </li>
      <li class="abn"><span class="abn-label">ABN</span>12 345 678 901</li>
    </ul>
  </article>

  <article class="card card-back" aria-label="Business card back">
    <svg class="card-bg" viewBox="0 0 540 340" preserveAspectRatio="none" aria-hidden="true">
      <defs>
        <linearGradient id="goldBack" x1="0" y1="0" x2="1" y2="0">
          <stop offset="0" stop-color="var(--gold-dark)"/>
          <stop offset="0.5" stop-color="var(--gold-light)"/>
          <stop offset="1" stop-color="var(--gold)"/>
        </linearGradient>
        <radialGradient id="purpleBack" cx="0.5" cy="0.5" r="0.7">
          <stop offset="0" stop-color="var(--magenta)"/>
          <stop offset="1" stop-color="var(--purple-deep)"/>
        </radialGradient>
      </defs>
      <rect width="540" height="340" fill="url(#purpleBack)"/>
      <rect y="98" width="540" height="124" fill="url(#goldBack)"/>
      <rect y="280" width="540" height="6" fill="var(--gold)"/>
      <rect y="300" width="540" height="12" fill="var(--gold)"/>
    </svg>

    <div class="brand">
      <span class="brand-square" aria-hidden="true"></span>
      <p class="brand-name"><span class="line-main">Ridgeway</span><span class="line-sub">Accommodation</span></p>
    </div>
  </article>

</main>
</body>
</html>
```